Business Card Design for an Investment Company

We need a business card design for our private investment company, called Ashbourne Partners. Ashbourne Partners is an investments partnership that aims to acquire shares in listed companies with a view to influencing those companies through active dialogue in order to improve their value. We need designs that use the logo colors (blue, grey, white), we need both English and Arabic on the business cards (can be on one side or 2 sides). The final logo should communicate professionalism, conservatism (nothing too fancy or too cheesy), that we are smart, conservative and old school.

Target Market(s)

Investment companies

Industry/Entity Type

Investment

Contact Information for Business Card

Khalid Yousef Rumaithi
Senior Executive Officer

Palm Terrace 07, Level 3, Office 215/12
HLMZ

+9714987650
krumaithi@ashbournepartners.com
www.ashbournepartners.com

Requirements
Must have
• Logo to be placed on the left hand side of the business card
• for the Arabic, we only need to have the name and title so it can be accomodated on one side so we can have the other side with full color and logo. The arabic that needs to be used is the below:
• خالد يوسف الرميثي
• المدير التنفيدي

```html
<!DOCTYPE html>
<html lang="en">
<head>
<meta charset="utf-8">
<title>Ashbourne Partners – Business Card</title>
<link href="https://fonts.googleapis.com/css2?family=Lato:wght@400;700&family=Noto+Naskh+Arabic:wght@400;700&display=swap" rel="stylesheet">
<style>
  :root {
    --backdrop: #2b2b2d;
    --brand-blue: #1670a6;
    --brand-grey: #5d5e61;
    --card-white: #ffffff;
    --text-grey: #4a4a4d;
    --rule-blue: #4f8fc0;
  }
  * { margin: 0; padding: 0; box-sizing: border-box; }
  html, body {
    width: 1200px; height: 880px; overflow: hidden;
    background: var(--backdrop);
    font-family: "Lato", sans-serif;
  }
  .canvas { position: relative; width: 1200px; height: 880px; }

  .card {
    position: absolute;
    width: 620px; height: 354px;
    box-shadow: 0 10px 28px rgba(0,0,0,.45);
  }
  .card--front { left: 90px; top: 70px; background: var(--brand-blue); }
  .card--back { left: 490px; top: 456px; background: var(--card-white); }

  .wordmark {
    position: absolute;
    display: flex; align-items: center; gap: 12px;
    font-family: "Lato", sans-serif; font-weight: 700;
    font-size: 36px; letter-spacing: -0.5px; white-space: nowrap;
  }
  .wordmark__square { width: 28px; height: 28px; background: var(--brand-grey); flex: none; }
  .card--front .wordmark { left: 56px; top: 154px; color: var(--card-white); }
  .card--back .wordmark { left: 54px; top: 44px; color: var(--brand-blue); font-size: 30px; }
  .card--back .wordmark__square { width: 24px; height: 24px; }

  .person { position: absolute; left: 56px; top: 110px; }
  .person__name { color: var(--brand-blue); font-weight: 700; font-size: 17px; line-height: 1.2; }
  .person__title { color: var(--text-grey); font-size: 14px; line-height: 1.2; }

  .person-ar {
    position: absolute; right: 34px; top: 100px;
    direction: rtl; text-align: right;
    font-family: "Noto Naskh Arabic", serif;
  }
  .person-ar__name { color: var(--brand-blue); font-weight: 700; font-size: 18px; line-height: 1.4; }
  .person-ar__title { color: var(--text-grey); font-size: 14px; line-height: 1.4; }

  .address {
    position: absolute; right: 34px; top: 176px;
    font-style: normal;
    text-align: right; color: var(--text-grey); font-size: 12.5px; line-height: 1.35;
  }

  .rule {
    position: absolute; left: 50px; right: 44px; top: 226px;
    height: 1px; background: var(--rule-blue);
  }

  .contacts { position: absolute; left: 54px; top: 244px; list-style: none; }
  .contacts__item {
    display: flex; align-items: center; gap: 6px;
    color: var(--text-grey); font-size: 13px; line-height: 1; margin-bottom: 6px;
  }
  .contacts__icon {
    width: 15px; height: 15px; background: var(--brand-blue);
    display: flex; align-items: center; justify-content: center; flex: none;
  }
</style>
</head>
<body>
<main class="canvas">

  <section class="card card--front" aria-label="Card front">
    <div class="wordmark"><span>Ashbourne Partners</span><span class="wordmark__square"></span></div>
  </section>

  <section class="card card--back" aria-label="Card back">
    <div class="wordmark"><span>Ashbourne Partners</span><span class="wordmark__square"></span></div>

    <div class="person">
      <p class="person__name">Khalid Yousef Rumaithi</p>
      <p class="person__title">Senior Executive Officer</p>
    </div>

    <div class="person-ar" lang="ar">
      <p class="person-ar__name">خالد يوسف الرميثي</p>
      <p class="person-ar__title">المدير التنفيدي</p>
    </div>

    <address class="address">
      Palm Terrace 07, Level 3, Office 215/12<br>HLMZ
    </address>

    <div class="rule"></div>

    <ul class="contacts">
      <li class="contacts__item">
        <span class="contacts__icon">
          <svg width="11" height="11" viewBox="0 0 24 24"><path fill="#fff" d="M6.6 10.8a15 15 0 0 0 6.6 6.6l2.2-2.2c.3-.3.7-.4 1-.2 1.1.4 2.3.6 3.6.6.6 0 1 .4 1 1V20c0 .6-.4 1-1 1A17 17 0 0 1 3 4c0-.6.4-1 1-1h3.5c.6 0 1 .4 1 1 0 1.3.2 2.5.6 3.6.1.3 0 .7-.2 1z"/></svg>
        </span>+9714987650
      </li>
      <li class="contacts__item">
        <span class="contacts__icon">
          <svg width="11" height="11" viewBox="0 0 24 24"><rect x="2" y="5" width="20" height="14" fill="none" stroke="#fff" stroke-width="2"/><path d="M2 6l10 7 10-7" fill="none" stroke="#fff" stroke-width="2"/></svg>
        </span>krumaithi@ashbournepartners.com
      </li>
      <li class="contacts__item">
        <span class="contacts__icon">
          <svg width="11" height="11" viewBox="0 0 24 24" fill="none" stroke="#fff" stroke-width="2"><circle cx="12" cy="12" r="9"/><path d="M3 12h18M12 3c3 3 3 15 0 18M12 3c-3 3-3 15 0 18"/></svg>
        </span>www.ashbournepartners.com
      </li>
    </ul>
  </section>

</main>
</body>
</html>
```